Visitenkarten-Design für Steuerberater und Wirtschaftsprüfer
Zielgruppe
Steuerberater, Wirtschaftsprüfer in München
Aufgabenstellung
Wir haben ein Logo das uns gefällt, jetzt allerdings steht die Umfirmierung vor der Tür und aus der Kanzlei Wendeholt (so unser Name) wird Wendeholt und Partner mbB (die Jugend kommt mit als Partner in die Kanzlei) , Steuerberater, Wirtschaftsprüfer
Analog unseres alten Briefpapiers und der alten Visitenkarten soll eigentlich nur der Zusatz 'und Partner mbB' oder '& Partner mbB' gestaltet werden.
Das Dateiformat bei Visitenkarten bitte so übergeben, dass wir Namen selbst austauschen mit gängigen Officeprogrammen austauschen können. Bei den Visitenkarten ist das große 'Wendeholt' geprägt.
Ich stelle das Logo, das aktuelle Briefpapier und aktuelle Visitenkarten ein. Unsere Farbe ist grau.
Das Logo bitte in .pdf, .png, .psd und .eps (sagt mi alles nichts, haben wir aber alles schon mal irgendwo gebraucht) , Visiten karten auch in .pddf und .ai
Bei Fragen kontaktiert mich gern jederzeit.

```html
<!DOCTYPE html>
<html lang="de">
<head>
<meta charset="utf-8">
<title>Wendeholt &amp; Partner mbB – Briefbogen Gestaltungsvorgabe</title>
<link rel="stylesheet" href="https://fonts.googleapis.com/css2?family=Arimo:wght@400;700&family=Roboto+Condensed:wght@400;700&family=Tinos&display=swap">
<style>
  :root {
    --paper: #fafafa;
    --band: #d2d3d5;
    --ink: #1d1d1b;
    --brand-grey: #5f5f5f;
    --meta-grey: #6e6e6e;
    --guide-red: #d22630;
    --dot: #9a9a9a;
  }
  html, body { margin: 0; padding: 0; overflow: hidden; background: var(--paper); }
  .sheet {
    position: relative; width: 856px; height: 1200px; overflow: hidden;
    background: var(--paper); color: var(--ink);
    font-family: "Arimo", Arial, sans-serif;
  }
  .abs { position: absolute; white-space: nowrap; }
  .band { position: absolute; background: var(--band); }

  /* letterhead */
  .brand { left: 326px; top: 40px; width: 206px; text-align: left; color: var(--brand-grey); }
  .brand__name { font-family: "Arimo", sans-serif; font-weight: 400; font-size: 37px; letter-spacing: 1px; line-height: 40px; }
  .brand__suffix { font-weight: 400; font-size: 17px; line-height: 20px; letter-spacing: .5px; border-bottom: 1px solid var(--brand-grey); padding-bottom: 1px; }
  .brand__tagline { font-weight: 400; font-size: 10.4px; line-height: 14px; letter-spacing: .2px; }
  .brand__rule { position: absolute; left: 548px; top: 42px; width: 2px; height: 72px; background: #fff; }

  /* letter content */
  .sender { left: 102px; top: 203px; font-family: "Roboto Condensed", sans-serif; font-size: 7.6px; color: var(--meta-grey); }
  .sender strong { font-weight: 700; }
  .address { left: 102px; top: 220px; font-size: 15.8px; line-height: 20.2px; }
  .date { right: 102px; top: 366px; font-size: 15.8px; }
  .subject { left: 102px; top: 403px; font-size: 20.5px; font-weight: 700; }
  .body { left: 102px; font-size: 15.8px; line-height: 20.2px; }

  /* guides */
  .guide { position: absolute; background: var(--guide-red); }
  .note { position: absolute; white-space: nowrap; font-family: "Tinos", "Times New Roman", serif; color: var(--guide-red); font-size: 17px; line-height: 20.6px; }
  .dot { position: absolute; width: 4px; height: 4px; border-radius: 50%; background: var(--dot); }

  /* footer */
  .footer { left: 0; width: 856px; top: 1150px; text-align: center; font-family: "Roboto Condensed", sans-serif; font-size: 12.6px; line-height: 15.6px; color: var(--meta-grey); }
  .footer strong { font-weight: 700; }
</style>
</head>
<body>
<div class="sheet">
  <!-- header bands and brand -->
  <div class="band" style="left:0;top:42px;width:305px;height:72px"></div>
  <div class="band" style="left:549px;top:42px;width:307px;height:72px"></div>
  <div class="abs brand">
    <div class="brand__name">WENDEHOLT</div>
    <div class="brand__suffix">&amp; PARTNER mbB</div>
    <div class="brand__tagline">STEUERBERATER | WIRTSCHAFTSPRÜFER</div>
  </div>
  <div class="brand__rule"></div>

  <!-- margin guides -->
  <div class="guide" style="left:101.5px;top:0;width:1px;height:224px"></div>
  <div class="note" style="left:110px;top:131px">55 mm</div>
  <div class="note" style="left:26px;top:201px">25 mm</div>
  <div class="guide" style="left:0;top:224px;width:102px;height:1px"></div>
  <div class="note" style="left:780px;top:201px">25 mm</div>
  <div class="guide" style="left:754px;top:224px;width:102px;height:1px"></div>
  <div class="note" style="left:26px;top:686px">25 mm</div>
  <div class="guide" style="left:0;top:709px;width:102px;height:1px"></div>
  <div class="note" style="left:780px;top:686px">25 mm</div>
  <div class="guide" style="left:754px;top:709px;width:102px;height:1px"></div>

  <div class="dot" style="left:20px;top:393px"></div>
  <div class="dot" style="left:20px;top:603px"></div>

  <!-- sender line and address -->
  <div class="abs sender"><strong>KANZLEI LENA S. WENDEHOLT</strong> | Lindenhof-Str. 22 | 80634 München</div>
  <div class="abs address">Musterfirma<br>Max Mustermann<br>Adresszusatz<br>Musterstraße 123<br>12345 Musterstadt<br>Musterland</div>

  <svg class="abs" style="left:244px;top:275px" width="84" height="12" viewBox="0 0 84 12">
    <line x1="6" y1="6" x2="84" y2="6" stroke="#d22630" stroke-width="1.2"/>
    <path d="M0 6 L7 1.5 L5.5 6 L7 10.5 Z" fill="#d22630"/>
  </svg>
  <div class="note" style="left:330px;top:260px">Anschriftenfeld:<br>75mm breit, 30mm hoch<br>Schrift: Arial, 11pt, 6 mögliche<br>Zeilen</div>

  <!-- letter body -->
  <div class="abs date">München, 00. Monat 2014</div>
  <div class="abs subject">Betreffzeile</div>
  <div class="abs body" style="top:466px">Sehr geehrter Herr Mustermann,</div>
  <div class="abs body" style="top:506px">Kurzer Brief an ein Idol. Lieber Onkel Bertram, schon lange wollte ich Dir sagen, daß ich<br>Dich für einen ganz tollen Texter halte. Ich weiß, Du hörst sehr gerne Lob, und deshalb kann<br>man nicht oft genug sagen, daß Du der Größte bist.</div>
  <div class="abs body" style="top:587px">Gerade in Deinem Alter ist man ja gesegnet, wenn man noch so witzig schreiben kann wie<br>Du. Viele Deiner Werberkollegen sind ja schon zu wichtig, um noch den Humor zu haben.</div>
  <div class="abs body" style="top:648px">Du bist da ganz anders. Du kannst richtig komisch sein. Und das, obwohl Du in Deinem sehr<br>langen Leben auch schon sehr viele unangenehme Dinge schreiben mußtest. Texte<br>für Burgerhaus Sonnweg zum Beispiel. Oder kleine Reime für Onkel Gernot. Nein, Du hast es<br>nicht leicht gehabt. Und dann noch die Selbstdarstellung für Tante Odile.</div>
  <div class="abs body" style="top:748px">Gerade in Deinem Alter ist man ja gesegnet, wenn man noch so witzig schreiben kann wie<br>Du. Viele Deiner Werberkollegen sind ja schon zu wichtig, um noch den Humor zu haben.</div>
  <div class="abs body" style="top:828px">Mit freundlichen Grüßen</div>
  <div class="abs body" style="top:909px">Vorname Name<br>Titel</div>

  <svg class="abs" style="left:562px;top:803px" width="12" height="82" viewBox="0 0 12 82">
    <line x1="6" y1="6" x2="6" y2="82" stroke="#d22630" stroke-width="1.2"/>
    <path d="M6 0 L10.5 7 L6 5.5 L1.5 7 Z" fill="#d22630"/>
  </svg>
  <div class="note" style="left:569px;top:894px">Textfeld:<br>160mm breit,180mm hoch<br>Schrift: Arial, 11pt (Betreff 14pt bold)</div>

  <!-- footer -->
  <div class="band" style="left:0;top:1153px;width:102px;height:41px"></div>
  <div class="band" style="left:754px;top:1153px;width:102px;height:41px"></div>
  <div class="abs footer">
    <strong>KANZLEI LENA S. WENDEHOLT</strong> | Lindenhof-Str. 22 | 80634 München<br>
    <strong>fon</strong> 089-47210355 | <strong>fax</strong> 089-47210366 | <strong>mail</strong> info@kanzlei-wendeholt.de | <strong>web</strong> www.kanzlei-wendeholt.de<br>
    <strong>UstID</strong> DE 204518377 | <strong>IBAN</strong> DE 12 7001 0080 0004 2217 63 | <strong>BIC</strong> ABCDDEM1XXX
  </div>
</div>
</body>
</html>
```